依頼詳細
既存のサイトを見ていただければ分かりやすいかと思いますが、

サロンのイメージカラーは、ブラウン+ゴールド、サロンのモチーフは白雪姫としており、リンゴとティアラを前面に出しています。

サロン名のルチェッタ(Lucetta)はイタリア語です。

見出しなどに使用する字体全ては、ロゴにあわせてください。

色味はブラウン+ゴールドに、薄めのピンク系、またはオレンジ系の組み合わせで、ゴールドの光沢度は、各デザイナー様にお任せいたします。

暖かい雰囲気で、高級感を前面に出しつつ、近寄りがたい雰囲気になり過ぎないデザインが希望です。

ゴシックより、明朝タイプ、角より、丸みがあるイメージを希望します。

幅広い年代から見られるので、タイトル部分などは、年配の方が見やすいよう、英語を小さめにしてカタカナ優勢でお願いします。

キラキラは必要ありませんが、まつ毛エクステに、ラメやラインストーンを使うことがあるので、ラインストーン、ラメがイメージ出来るものをデザインに組み込んでいただければ、想像しているイメージに近くなります。
サイトURL
http://www.eye-lucetta-example.com/
ページ数
2ページ
希望イメージ
シンプル 複雑
単色 カラフル
暗い 明るい
日常 高級
遊び心 厳粛
未来的 伝統的
女性的 男性的
希望する色
ブラウン+ゴールドに、薄めのピンク系、またはオレンジ系
納品ファイル
• 高解像度JPG (.jpg)
• イラストレーター形式 (.ai)
• フォトショップ形式 (.psd)
補足説明
詳細はPDFをダウンロードしてください。
申し訳ありません。

PDFに間違いがありましたので、新たに添付しました。
資料にある納品物に関して、psd、aiとありますが、双方納品ではなく、どちらかの形式で問題ございません。
選定確約を追加しました。
■ 選んだ理由

ご提案をいただいたデザインは全てすばらしく、サロン様も長い時間迷っていましたが、

迷いに迷った末、こちらの提案を選ばせていただきました。

この提案はこちらの指定した色合いにとらわれず、

あえて全く違う色を使った提案になっていたのですが、

ルチェッタの「幅広い年代層」から考えていただいた、

見やすさ、

さらに言うと

ユーザビリティを重視した、デザインと色使いにとても満足していらっしゃいました。

■ 提案者全員のお礼・コメント

ご提案いただきましたデザインは、当選したデザイン以外は、どれも、こちらの指定どおり忠実に考えていただき、非常に満足いくものでした。

サロン様も、どれもイメージに近かったので本当に迷ったと、おっしゃっていましたが、1つだけ異色のデザインが目につき心に残ったようです。

ご提案していただきました皆様、この度は本当にありがとうございました。

またご縁がありましたらよろしくお願い致します。

```html
<!DOCTYPE html>
<html lang="ja">
<head>
<meta charset="utf-8">
<title>ルチェッタ | アイラッシュサロン</title>
<link rel="stylesheet" href="https://fonts.googleapis.com/css2?family=Noto+Serif+JP:wght@400;600;700&family=Cormorant+Garamond:ital,wght@0,500;0,600;1,500&display=swap">
<style>
:root{
  --brown:#4e3320;
  --brown-mid:#7a5536;
  --gold:#c6a15b;
  --gold-light:#e6cf98;
  --gold-pale:#f4e9cf;
  --cream:#fbf7ee;
  --beige:#efe3c9;
  --pink:#f5d9d2;
  --pink-deep:#d88f86;
  --orange:#e9a24c;
  --text:#4a3a2e;
  --muted:#8c7b6b;
  --line:#e3d5b8;
  --white:#ffffff;
}
*{box-sizing:border-box;margin:0;padding:0}
html,body{width:739px;height:1200px;overflow:hidden}
body{font-family:"Noto Serif JP",serif;color:var(--text);background:var(--white);font-size:9px;line-height:1.5}
.en{font-family:"Cormorant Garamond",serif}
.page{width:739px;height:1200px;display:flex;flex-direction:column}

/* header */
.site-header{height:74px;display:flex;align-items:center;justify-content:space-between;padding:0 22px;background:linear-gradient(#fff,#faf5ea)}
.brand{display:flex;align-items:center;gap:10px}
.brand-name{font-family:"Cormorant Garamond",serif;font-weight:600;font-size:30px;color:var(--brown);letter-spacing:1px}
.brand-sub{font-size:8px;color:var(--muted)}
.header-info{text-align:right}
.header-note{font-size:7px;color:var(--muted);margin-bottom:4px}
.header-contact{display:flex;align-items:center;gap:8px;justify-content:flex-end}
.tel-tag{border:1px solid var(--brown-mid);font-size:7px;padding:1px 4px;color:var(--brown-mid)}
.tel{font-size:17px;font-weight:700;color:var(--brown)}
.tel small{font-size:9px}
.reserve-btn{background:linear-gradient(var(--brown-mid),var(--brown));color:var(--gold-light);font-size:8px;padding:5px 12px;border-radius:3px}
.tel-hours{font-size:6.5px;color:var(--muted);margin-top:2px}

/* hero */
.hero{height:209px;position:relative;background:linear-gradient(100deg,#e9d2a8 0%,#d8b57b 35%,#f3e3c0 62%,#fbf3e2 100%)}
.hero-photo{position:absolute;inset:0 280px 0 0;background:linear-gradient(160deg,#e0c390,#b88a55 55%,#8f653c)}
.hero-copy{position:absolute;right:40px;top:62px;width:250px;font-size:11px;line-height:1.9;color:var(--brown)}

/* nav */
.global-nav{height:32px;background:linear-gradient(#d9b878,#b48a45);display:flex;justify-content:space-around;align-items:center;padding:0 30px;border-bottom:2px solid var(--gold-light)}
.global-nav a{color:var(--white);font-size:9px;text-decoration:none}

main{padding:0 22px}
.section-title{font-size:12px;font-weight:600;color:var(--brown);border-bottom:1px solid var(--line);padding-bottom:4px;margin-bottom:8px}

/* designs */
.designs{display:flex;gap:12px;margin-top:16px;height:160px}
.designs-body{flex:1}
.design-list{display:grid;grid-template-columns:repeat(3,1fr);gap:6px 10px}
.design-item{display:flex;align-items:center;gap:5px}
.design-item .en{font-style:italic;font-size:13px;color:var(--brown)}
.design-item .eye{width:58px;height:16px;border-radius:8px;background:linear-gradient(90deg,#d9c3a9,#8a6b55)}
.design-item small{font-size:7px;color:var(--muted)}
.design-note{font-size:7px;color:var(--muted);margin-top:12px}
.more{font-size:7px;color:var(--brown-mid);text-align:right;margin-top:4px}
.designs-photo{width:146px;height:100px;margin-top:22px;background:linear-gradient(135deg,#efdcd0,#a88670)}

/* event banner */
.event{height:72px;margin-top:6px;border:1px solid var(--gold-light);background:linear-gradient(90deg,#fdf6e8,#f7e6c6);display:flex;align-items:center;padding:0 22px;gap:20px}
.event-label{font-family:"Cormorant Garamond",serif;font-style:italic;font-size:18px;color:var(--brown-mid)}
.event-date{font-size:18px;font-weight:700;color:var(--pink-deep)}
.event-date small{font-size:11px}
.event-tag{background:var(--orange);color:#fff;font-size:8px;padding:4px;border-radius:50%;width:34px;height:34px;display:flex;align-items:center;justify-content:center;text-align:center;line-height:1.1}
.event-title{font-size:20px;font-weight:700;color:var(--pink-deep)}

/* promo row */
.promo{display:flex;gap:10px;margin-top:10px;height:150px}
.trial{flex:1;background:linear-gradient(135deg,#fbe8e3,var(--pink));border:1px solid #efc6bd;position:relative;padding:14px 18px}
.trial-title{font-size:14px;font-weight:700;color:var(--brown)}
.trial-price{display:flex;align-items:center;gap:10px;margin-top:18px;color:var(--pink-deep)}
.trial-price .old{font-size:14px;line-height:1.2;color:var(--brown-mid)}
.trial-price .new{font-size:40px;font-weight:700}
.trial-price .new small{font-size:16px}
.trial-badge{position:absolute;right:16px;top:10px;font-family:"Cormorant Garamond",serif;font-style:italic;font-size:12px;color:var(--pink-deep)}
.tiles{width:270px;display:grid;grid-template-columns:1fr 1fr;gap:6px}
.tile{border:1px solid var(--line);display:flex;align-items:center;justify-content:center;font-size:9px;color:var(--brown);background:var(--cream);gap:5px}
.tile-photo{background:linear-gradient(135deg,#f1e0d6,#c9a58a)}
.tile-sns{background:#6fb3cf;color:#fff;font-size:12px}
.tile svg{width:14px;height:14px}

/* news */
.news{margin-top:12px;height:190px}
.news-item{display:flex;gap:10px;padding:8px 0;border-bottom:1px dotted var(--line)}
.news-date{width:70px;color:var(--muted);font-size:8px}
.news-tag{background:var(--gold);color:#fff;font-size:7px;padding:0 5px;height:13px;border-radius:2px}
.news-text{flex:1;font-size:8px}
.news-text strong{color:var(--brown);display:block;font-weight:600}
.news-more{font-size:7px;color:var(--brown-mid);text-align:center;margin-top:6px}

/* payment */
.payment{display:flex;align-items:center;gap:10px;height:36px;border-top:1px solid var(--line);margin-top:6px}
.payment span{font-size:8px;color:var(--muted)}
.card{width:34px;height:20px;border-radius:3px;background:var(--beige);border:1px solid var(--line)}

/* footer */
.site-footer{margin-top:auto;background:var(--beige);height:196px;display:flex;flex-direction:column}
.footer-inner{flex:1;display:flex;padding:16px 22px;gap:20px}
.footer-brand{width:200px}
.footer-brand .brand-name{font-size:24px}
.footer-address{font-size:7px;color:var(--muted);margin-top:6px;line-height:1.7}
.footer-contact{width:170px}
.footer-contact .tel{font-size:15px}
.footer-contact .reserve-btn{display:inline-block;margin-top:6px}
.footer-links{flex:1;display:grid;grid-template-columns:1fr 1fr;gap:3px 10px;font-size:8px;color:var(--brown)}
.footer-links li{list-style:none}
.footer-links li::before{content:"› ";color:var(--gold)}
.copyright{background:var(--brown);color:var(--gold-light);font-size:7px;text-align:right;padding:5px 22px}
</style>
</head>
<body>
<div class="page">
  <header class="site-header">
    <div class="brand">
      <span class="brand-name">Lucetta</span>
      <span class="brand-sub">アイラッシュサロン ルチェッタ</span>
    </div>
    <div class="header-info">
      <p class="header-note">まつげエクステ専門店・自然な仕上がりをご提案します</p>
      <div class="header-contact">
        <span class="tel-tag">ご予約</span>
        <span class="tel"><small>TEL</small> 045-000-1234</span>
        <span class="reserve-btn">ご予約・お問い合わせ</span>
      </div>
      <p class="tel-hours">営業時間 10:00〜20:00 / 定休日 不定休</p>
    </div>
  </header>

  <section class="hero">
    <div class="hero-photo" role="img" aria-label="落ち着いた照明のサロン施術室とリクライニングチェア"></div>
    <p class="hero-copy">お客様の目元の表情に合わせて、一本一本丁寧にデザインしていくことで、自然な仕上がりをご提供いたします。</p>
  </section>

  <nav class="global-nav">
    <a>ホーム</a><a>メニュー&amp;料金</a><a>デザイン</a><a>施術の流れ</a><a>店舗案内</a><a>Q&amp;A</a><a>ご予約&amp;アクセス</a>
  </nav>

  <main>
    <section class="designs">
      <div class="designs-body">
        <h2 class="section-title">ルチェッタがご提案するデザインは全部で5種類</h2>
        <div class="design-list">
          <div class="design-item"><span class="en">Princess</span><small>プリンセス</small><span class="eye" role="img" aria-label="目元の写真"></span></div>
          <div class="design-item"><span class="en">Rosette</span><small>ロゼット</small><span class="eye" role="img" aria-label="目元の写真"></span></div>
          <div class="design-item"><span class="en">Aurelie</span><small>オーレリー</small><span class="eye" role="img" aria-label="目元の写真"></span></div>
          <div class="design-item"><span class="en">Celeste</span><small>セレステ</small><span class="eye" role="img" aria-label="目元の写真"></span></div>
          <div class="design-item"><span class="en">Marine</span><small>マリーン</small><span class="eye" role="img" aria-label="目元の写真"></span></div>
        </div>
        <p class="design-note">お好みの長さや本数に合わせて、目元の形にぴったりのデザインをお選びいただけます。</p>
        <p class="more">» 詳しく見る</p>
      </div>
      <div class="designs-photo" role="img" aria-label="まつげエクステを施した目元のクローズアップ"></div>
    </section>

    <section class="event">
      <span class="event-label">New Events!</span>
      <span class="event-date">9/4<small>(木)</small> 00:00〜00:00</span>
      <span class="event-tag">期間<br>限定</span>
      <span class="event-title">増毛キャンペーン!</span>
    </section>

    <section class="promo">
      <div class="trial">
        <span class="trial-badge">Special Price!</span>
        <p class="trial-title">初回限定お試しキャンペーン</p>
        <div class="trial-price">
          <p class="old">100本<br>¥3,000円</p>
          <svg width="22" height="22" viewBox="0 0 22 22"><path d="M4 6 L12 11 L4 16 Z M11 6 L19 11 L11 16 Z" fill="currentColor"/></svg>
          <p class="new">6,500<small>円</small></p>
        </div>
      </div>
      <div class="tiles">
        <div class="tile">ブライダルコース</div>
        <div class="tile">24時間ネット予約</div>
        <div class="tile tile-photo" role="img" aria-label="スタッフブログの写真"></div>
        <div class="tile tile-sns">@Lucetta</div>
        <div class="tile">
          <svg viewBox="0 0 14 14"><circle cx="7" cy="7" r="6" fill="none" stroke="currentColor"/><path d="M6 4 L9 7 L6 10" fill="none" stroke="currentColor"/></svg>
          プロフィール
        </div>
        <div class="tile">スタッフ紹介</div>
      </div>
    </section>

    <section class="news">
      <h2 class="section-title">お知らせ</h2>
      <div class="news-item">
        <span class="news-date">2013年0月00日</span><span class="news-tag">キャンペーン</span>
        <p class="news-text"><strong>ホームページを開設しました</strong>ルチェッタのホームページをリニューアルいたしました。今後とも最新情報をお届けいたします。</p>
      </div>
      <div class="news-item">
        <span class="news-date">2013年0月00日</span><span class="news-tag">お知らせ</span>
        <p class="news-text"><strong>増毛キャンペーンのお知らせ</strong>期間限定で増毛メニューをお得な価格でご提供いたします。ぜひこの機会にご利用ください。</p>
      </div>
      <p class="news-more">» お知らせ一覧を見る</p>
    </section>

    <section class="payment">
      <span>各種クレジットカード使えます</span>
      <span class="card"></span><span class="card"></span><span class="card"></span><span class="card"></span><span class="card"></span>
    </section>
  </main>

  <footer class="site-footer">
    <div class="footer-inner">
      <div class="footer-brand">
        <span class="brand-name">Lucetta</span>
        <p class="footer-address">〒000-0000 神奈川県横浜市○○区○○町0-0-0<br>○○ビル 2F<br>駅より徒歩3分</p>
      </div>
      <div class="footer-contact">
        <span class="tel">TEL 045-000-1234</span>
        <p class="tel-hours">営業時間 10:00〜20:00</p>
        <span class="reserve-btn">ご予約・お問い合わせ</span>
      </div>
      <ul class="footer-links">
        <li>ホーム</li><li>スタッフ紹介</li>
        <li>メニュー&amp;料金</li><li>会社概要</li>
        <li>デザイン</li><li>プライバシーポリシー</li>
        <li>施術の流れ</li><li>サイトマップ</li>
        <li>店舗案内</li><li>Q&amp;A</li>
      </ul>
    </div>
    <p class="copyright">Copyright © Eyelash Salon Lucetta All Rights Reserved.</p>
  </footer>
</div>
</body>
</html>
```